Medical Software Informational Flyer and Website Design

Our company, Copper Vale Systems, is launching a new product, the Copper Vale Practice Hub. It is a software suite that will increase the productivity and volume of a LASIK practice.

We want this flyer to be a companion to our big reveal presentation at OLV and PEMWG; it's primary purpose is to inform potential clients on the many ways this software will help their practice. It is also obviously a promotional material. Because it is a companion to our presentation, we feel that it is acceptable for the flyer to contain much more text than would normally be reasonable in a flyer; it will go into more detail about the 12 major selling points of our software than our presentation time will allow. Having said that, however, we still want there to be "breathing room" for the design and the viewer's eyes.

We have uploaded our logo, both in full color and in white with no background (often used for watermarks, but certainly not restricted for that use alone). Our logo should be accompanied by either "Copper Vale Systems" or "Copper Vale" using the Trajan Pro font (unoriginal, we know, but it's what we've chosen). We have included a color palette that compliments our logo, but designs are not limited to that palette (for example, we have found a pink (#cc1448) that compliments the palette and that we have used in the presentation).

We have also uploaded a PSD that includes icons that could compliment 9 of the 12 major selling points for the Copper Vale Practice Hub software (the category titles are subject to change). The icons are not necessarily set in stone. For consistency with our presentation, the Protection, Integration, and Review icons should be used, but any of the remaining six (in particular, the Personalized icon) can be changed to whatever you think might be more suitable. The PSD also has some preliminary text for a few of the 12 selling points (we are refining the text now and will get the final content to designers very soon). Also note that the font is simply a placeholder; use whatever font you think would best compliment your design. Finally, keep in mind that the PSD does NOT reflect a design we are looking for; in fact, we hate this "design" and hesitate to call it a design. It was simply a way to arrange the elements to easily distribute them to designers.

We want an 8 1/2in x 11in 8-page flyer that is professional, simple, and has a clear message: this product will revolutionize your practice! We of course also need a website design that compliments the flyer design once the flyer design is finalized and chosen.

We will be monitoring this project closely-- please ask any questions you have!
Updates

Target Market(s)

Physicians, technicians, and marketing personnel in the LASIK industry.

Industry/Entity Type

Software

Number of Pages Required

4 page

Font styles to use
Serif
Sans Serif

```html
<!DOCTYPE html>
<html lang="en">
<head>
<meta charset="utf-8">
<title>Copper Vale Practice Hub – Flyer</title>
<link rel="stylesheet" href="https://fonts.googleapis.com/css2?family=Roboto+Condensed:wght@400;700&family=Cinzel:wght@400&display=swap">
<style>
  :root {
    --header-top: #1e9276;
    --header-bottom: #127060;
    --navy: #0a2a3c;
    --body-top: #0e3c52;
    --body-bottom: #0b3247;
    --rule: #e4c51f;
    --accent: #e9dc3a;
    --text: #ffffff;
    --footer: #167a62;
    --hump: #178a6c;
  }
  * { margin: 0; padding: 0; box-sizing: border-box; }
  html, body { width: 927px; height: 1200px; overflow: hidden; background: var(--body-bottom); }
  .flyer {
    position: relative;
    width: 927px;
    height: 1200px;
    overflow: hidden;
    background: linear-gradient(180deg, var(--body-top), var(--body-bottom));
    font-family: "Roboto Condensed", "Arial Narrow", sans-serif;
    color: var(--text);
  }
  .masthead {
    position: absolute;
    left: 0; top: 0;
    width: 927px; height: 176px;
    background: linear-gradient(180deg, var(--header-top), var(--header-bottom));
  }
  .masthead-curve { position: absolute; right: 0; top: 0; }
  .intro {
    position: absolute;
    left: 21px; top: 24px;
    width: 660px;
    font-size: 18.5px;
    line-height: 35px;
  }
  .brand {
    position: absolute;
    right: 22px; top: 62px;
    font-size: 19px;
    font-weight: 700;
    color: var(--text);
  }
  .masthead-rule {
    position: absolute;
    left: 0; top: 176px;
    width: 927px; height: 3px;
    background: var(--rule);
  }
  .feature-icon { position: absolute; }
  .fingerprint {
    position: absolute;
    width: 82px; height: 98px;
    border-radius: 42px 42px 38px 38px;
    background: radial-gradient(ellipse at 50% 45%, #f2f6f8 0%, #b9cad3 70%, #7e98a6 100%);
    opacity: 0.9;
  }
  .feature {
    position: absolute;
    left: 155px;
    width: 742px;
    font-size: 18.6px;
    line-height: 30.6px;
  }
  .feature-lead { line-height: 32.6px; }
  .feature .highlight { color: var(--accent); font-weight: 700; }
  .footer {
    position: absolute;
    left: 0; bottom: 0;
    width: 927px; height: 39px;
    background: var(--footer);
  }
  .footer-url {
    position: absolute;
    right: 8px; top: 9px;
    font-family: "Cinzel", Georgia, serif;
    font-size: 17px;
    letter-spacing: 0.5px;
    color: var(--text);
  }
</style>
</head>
<body>
<main class="flyer">
  <header class="masthead">
    <svg class="masthead-curve" width="290" height="176" viewBox="0 0 290 176" aria-hidden="true">
      <path d="M0 0 H290 V176 H250 C248 120 210 70 150 52 C90 34 30 20 0 0 Z" fill="var(--navy)"/>
      <path d="M110 176 C130 120 190 92 290 100 V176 Z" fill="var(--hump)"/>
    </svg>
    <p class="intro">Intro text here Intro text here Intro text here Intro text here Intro text here Intro text here Intro text here Intro text here Intro text here \ Intro text here Intro text here Intro text here Intro text here Intro text here Intro text here Intro text here Intro text here</p>
    <div class="brand">Copper Vale Systems</div>
  </header>
  <div class="masthead-rule"></div>

  <svg class="feature-icon" style="left:42px; top:235px" width="80" height="64" viewBox="0 0 80 64" aria-hidden="true">
    <path d="M0 12 H30 V0 L52 20 L30 40 V28 H0 Z" fill="#ffffff"/>
    <path d="M80 36 H50 V24 L28 44 L50 64 V52 H80 Z" fill="#ffffff"/>
  </svg>
  <p class="feature feature-lead" style="top:212px">It's time for a revolution in an industry that depends on effective marketing, tracking marketing campaign effectiveness, and converting interest into procedures. Finally comes the solution: the Copper Vale Practice Hub which includes <span class="highlight">connectivity</span> between your marketing records and your patient records. Two databases, one for patients and one for prospective patients, with a single program connecting them. It's simple, it's HIPAA-compliant, and it's only the beginning.</p>

  <div class="fingerprint" style="left:33px; top:442px" role="img" aria-label="Fingerprint icon for personalized communications"></div>
  <p class="feature" style="top:439px">Contact with prospective and current patients is key in a market of &nbsp;elective procedures. Communication must be efficient, standardized, but also <span class="highlight">personalized</span>, The Copper Vale Practice Hub does it all by incorporating the patient and contact database information in your communications. The Suite offers an array of customizable, personalized emails, texts, and even printouts for appointment reminders, surgery preparation information, and referral programs - all with a few clicks.</p>

  <div class="fingerprint" style="left:33px; top:688px" role="img" aria-label="Fingerprint icon for personalized communications"></div>
  <p class="feature" style="top:684px">Contact with prospective and current patients is key in a market of &nbsp;elective procedures. Communication must be efficient, standardized, but also <span class="highlight">personalized</span>, The Copper Vale Practice Hub does it all by incorporating the patient and contact database information in your communications. The Suite offers an array of customizable, personalized emails, texts, and even printouts for appointment reminders, surgery preparation information, and referral programs - all with a few clicks.</p>

  <div class="fingerprint" style="left:33px; top:918px" role="img" aria-label="Fingerprint icon for personalized communications"></div>
  <p class="feature" style="top:912px">Contact with prospective and current patients is key in a market of &nbsp;elective procedures. Communication must be efficient, standardized, but also <span class="highlight">personalized</span>, The Copper Vale Practice Hub does it all by incorporating the patient and contact database information in your communications. The Suite offers an array of customizable, personalized emails, texts, and even printouts for appointment reminders, surgery preparation information, and referral programs - all with a few clicks.</p>

  <footer class="footer">
    <span class="footer-url">WWW.WEBSITE TEXT.COM</span>
  </footer>
</main>
</body>
</html>
```